Brightwave Business Card

Professional Business Card Design required using the attached contact information.

Contact information can be rearranged as required.

The company is a new start up venture developing solar systems, the branding should be in keeping with that of one of the investors whose website is as follows https://www.quorvex.com/

```html
<!DOCTYPE html>
<html lang="en">
<head>
<meta charset="utf-8">
<title>Brightwave Renewables – Business Card</title>
<link rel="stylesheet" href="https://fonts.googleapis.com/css2?family=Montserrat:wght@500;600&family=Arimo:wght@400&family=Noto+Serif:wght@700&display=swap">
<style>
  :root {
    --page-bg: #d9dde1;
    --card-white: #ffffff;
    --ink: #1b1d22;
    --navy: #1f2a3a;
    --steel-blue: #3f9ab6;
    --teal: #2a7a6c;
    --forest: #1e6652;
    --silver: #c3c9cc;
    --pattern-tint: #f1f3f4;
  }
  * { box-sizing: border-box; margin: 0; padding: 0; }
  html, body {
    width: 1200px; height: 900px; overflow: hidden;
    background: var(--page-bg);
  }
  .canvas {
    width: 1200px; height: 900px;
    display: flex; align-items: center; justify-content: center; gap: 40px;
  }
  .card {
    position: relative;
    width: 540px; height: 309px;
    border-radius: 4px; overflow: hidden;
    box-shadow: 0 10px 28px rgba(20, 30, 40, 0.22);
  }

  /* Back side */
  .card-back {
    background:
      radial-gradient(ellipse at 52% 48%, var(--steel-blue) 0%, rgba(63,154,182,0) 45%),
      linear-gradient(135deg, var(--navy) 0%, #24506a 45%, var(--teal) 75%, var(--forest) 100%);
    display: flex; align-items: center; justify-content: center; gap: 14px;
  }
  .back-wordmark {
    font-family: "Montserrat", sans-serif; font-weight: 500;
    font-size: 30px; letter-spacing: 4px; color: var(--silver);
  }
  .back-dot {
    width: 12px; height: 12px; border-radius: 50%; background: var(--silver);
  }

  /* Front side */
  .card-front { background: var(--card-white); }
  .name-pattern {
    position: absolute; inset: 0;
    background: linear-gradient(180deg, var(--card-white) 0%, var(--pattern-tint) 100%);
  }
  .front-content {
    position: absolute; left: 0; right: 0; top: 26px;
    display: flex; flex-direction: column; align-items: center;
  }
  .front-wordmark {
    font-family: "Montserrat", sans-serif; font-weight: 600;
    font-size: 29px; letter-spacing: 3px; color: var(--ink);
  }
  .holder-name {
    margin-top: 16px;
    font-family: "Noto Serif", serif; font-weight: 700;
    font-variant: small-caps; font-size: 22px; letter-spacing: 1.5px;
    color: var(--forest);
  }
  .divider {
    width: 130px; height: 1px; margin-top: 6px;
    background: linear-gradient(90deg, rgba(30,102,82,0), var(--forest), rgba(30,102,82,0));
  }
  .contact-icons { display: flex; gap: 14px; margin-top: 7px; }
  .contact-icons svg { width: 14px; height: 14px; }
  .contact-list {
    list-style: none; margin-top: 8px; text-align: center;
    font-family: "Arimo", sans-serif; font-size: 12.5px; line-height: 1.5; color: var(--ink);
  }
  .company-band {
    position: absolute; left: 0; right: 0; bottom: 22px; height: 30px;
    display: flex;
  }
  .band-tab { width: 36px; background: var(--navy); margin-right: 5px; }
  .band-main {
    flex: 1;
    background: linear-gradient(90deg, var(--navy) 0%, #2d6a82 55%, var(--forest) 100%);
    display: flex; align-items: center; padding-left: 18px;
    font-family: "Montserrat", sans-serif; font-weight: 600;
    font-size: 13px; letter-spacing: 4px; color: #ffffff;
  }
</style>
</head>
<body>
<main class="canvas">
  <section class="card card-back" aria-label="Business card back">
    <span class="back-dot" aria-hidden="true"></span>
    <span class="back-wordmark">BRIGHTWAVE RENEWABLES</span>
  </section>

  <section class="card card-front" aria-label="Business card front">
    <div class="name-pattern" role="img" aria-label="Faint repeated company name pattern"></div>
    <div class="front-content">
      <div class="front-wordmark">BRIGHTWAVE RENEWABLES</div>
      <div class="holder-name">Daniel Corwin</div>
      <div class="divider"></div>
      <div class="contact-icons" aria-hidden="true">
        <svg viewBox="0 0 16 16"><path d="M4 1.5l2.2 3-1.3 1.6c.8 1.8 2.2 3.2 4 4l1.6-1.3 3 2.2-1.2 2.3C7 13.3 2.7 9 2 3.7z" fill="none" stroke="#1e6652" stroke-width="1.3"/></svg>
        <svg viewBox="0 0 16 16"><rect x="1.5" y="3.5" width="13" height="9" fill="none" stroke="#1e6652" stroke-width="1.3"/><path d="M1.5 3.5L8 9l6.5-5.5" fill="none" stroke="#1e6652" stroke-width="1.3"/></svg>
        <svg viewBox="0 0 16 16"><path d="M8 15s5-5 5-8.5a5 5 0 00-10 0C3 10 8 15 8 15z" fill="none" stroke="#1e6652" stroke-width="1.3"/><circle cx="8" cy="6.5" r="1.8" fill="#1e6652"/></svg>
      </div>
      <ul class="contact-list">
        <li>+1 (555) 014-2276</li>
        <li>daniel.corwin@brightwave-renewables.com</li>
        <li>210 Harbor Street, Portland, ME 04101</li>
      </ul>
    </div>
    <div class="company-band">
      <div class="band-tab"></div>
      <div class="band-main">BRIGHTWAVE RENEWABLES LLC</div>
    </div>
  </section>
</main>
</body>
</html>
```